Bright Tooth Dentistry Business Card

We need business cards for our dental office.
We are looking for a clean, elegant design

We provide dental services to children.
Our card needs to be appealing to referring dentists, parents and our team

Target Market(s)

referring dentists, parents and our team

Industry/Entity Type

Dental Clinic

Contact Information for Business Card

4816 Juniper Lane, Suite 240
Linden Brook, PA 15237

412-837-2961 Voice
412-837-2962 fax
info@brighttoothdentalpa.com email
www.brighttoothdentalpa.com web

Font styles to use
Sans Serif

Requirements
Must have
• White background - clean, crisp, elegant, simple
• rounded corners
• different color palate - once we come up with design, we will replace the blue with orange, green,
Nice to have
• Follow our logo typeface and colors
• then we can replace color

```html
<!DOCTYPE html>
<html lang="en">
<head>
<meta charset="utf-8">
<title>Bright Tooth Dentistry – Business Card</title>
<link rel="stylesheet" href="https://fonts.googleapis.com/css2?family=Montserrat:wght@600;700&family=Open+Sans:wght@400&display=swap">
<style>
  :root {
    --page-bg: #f3f4f6;
    --card-bg: #ffffff;
    --card-edge: #e3e5e8;
    --brand-blue: #2f9ad6;
    --ink: #111111;
    --ink-soft: #2b2b2b;
  }
  * { box-sizing: border-box; margin: 0; padding: 0; }
  html, body {
    width: 1200px;
    height: 849px;
    overflow: hidden;
    background: var(--page-bg);
  }
  .canvas {
    position: relative;
    width: 1200px;
    height: 849px;
    display: flex;
    align-items: center;
    justify-content: center;
    gap: 50px;
  }
  .card {
    position: relative;
    width: 525px;
    height: 300px;
    background: var(--card-bg);
    border: 1px solid var(--card-edge);
    border-radius: 24px;
    box-shadow: 0 6px 18px rgba(0, 0, 0, 0.06);
  }

  /* Front */
  .card-front {
    display: flex;
    flex-direction: column;
    align-items: center;
    justify-content: center;
    gap: 16px;
  }
  .brand-dot {
    width: 54px;
    height: 54px;
    border-radius: 50%;
    background: var(--brand-blue);
    flex-shrink: 0;
  }
  .brand-name {
    font-family: "Montserrat", sans-serif;
    font-weight: 600;
    color: var(--brand-blue);
    font-size: 34px;
    letter-spacing: 0.2px;
    white-space: nowrap;
  }

  /* Back */
  .card-back .brand-small {
    position: absolute;
    top: 40px;
    right: 34px;
    display: flex;
    align-items: center;
    gap: 8px;
  }
  .card-back .brand-small .brand-dot {
    width: 18px;
    height: 18px;
  }
  .card-back .brand-small .brand-name {
    font-size: 17px;
  }
  .contact {
    position: absolute;
    left: 40px;
    bottom: 40px;
  }
  .contact-address {
    font-family: "Montserrat", sans-serif;
    font-weight: 700;
    font-size: 13.5px;
    line-height: 1.35;
    color: var(--ink);
    margin-bottom: 10px;
    white-space: nowrap;
  }
  .contact-lines {
    list-style: none;
    font-family: "Open Sans", sans-serif;
    font-size: 12.5px;
    line-height: 1.45;
    color: var(--ink-soft);
    padding-left: 6px;
    white-space: nowrap;
  }
</style>
</head>
<body>
  <main class="canvas">
    <section class="card card-front" aria-label="Business card front">
      <span class="brand-dot" aria-hidden="true"></span>
      <span class="brand-name">Bright Tooth Dentistry</span>
    </section>

    <section class="card card-back" aria-label="Business card back">
      <div class="brand-small">
        <span class="brand-dot" aria-hidden="true"></span>
        <span class="brand-name">Bright Tooth Dentistry</span>
      </div>
      <div class="contact">
        <p class="contact-address">4816 Juniper Lane, Suite 240<br>Linden Brook, PA 15237</p>
        <ul class="contact-lines">
          <li>T: 412-837-2961</li>
          <li>F: 412-837-2962</li>
          <li>E: info@brighttoothdentalpa.com</li>
          <li>W: www.brighttoothdentalpa.com</li>
        </ul>
      </div>
    </section>
  </main>
</body>
</html>
```